Private School Marketing Package Folder

We are a Montessori Private School in Brampton, Ontario, Canada. Our website is www.vtschool.org. We need a graphic design for the folder that will hold our forms and other papers (all papers will be 8.5x11). So, the design should cover front, back, and the two flaps within. The back side within should be blank.
Updates

Please do look at the samples that I have uploaded. I want something very similar to that.

I really like the recent submissions but I am still looking for the 'clincher'. The clincher will have a bit less color (mostly white) and will look a lot like the sample I have posted.

Target Market(s)

Parents of children (K-12)

Industry/Entity Type

Graphic Design

Requirements
Must have
• Logo, a message, an image, nice colors.
Nice to have
• The two messages that I would like:
“The Creator inscribed within us the course that we must stay on”
-Sant Orvel Tahrik Sai

“Within the child is the person he or she will become”
- Dr. Helga Brunvaldi
Should not have
• Dont' want it to be too busy.

```html
<!DOCTYPE html>
<html lang="en">
<head>
<meta charset="utf-8">
<title>Valtrin Children's School – Folder Cover</title>
<link rel="stylesheet" href="https://fonts.googleapis.com/css2?family=Source+Sans+3:ital,wght@0,400;0,600;1,400;1,600&display=swap">
<style>
  :root {
    --paper: #ffffff;
    --cream: #fdf1de;
    --sun: #fbd592;
    --amber: #f6aa5c;
    --coral: #ee5d50;
    --plum: #8a506e;
    --navy: #4a4e8a;
    --mist: #b9bbd6;
    --ink: #111111;
    --wing-orange: #e67a2a;
    --wing-deep: #b8561c;
    --ghost: rgba(255, 255, 255, 0.2);
  }
  html, body {
    margin: 0;
    padding: 0;
    width: 1200px;
    height: 800px;
    overflow: hidden;
    background: var(--paper);
  }
  .folder {
    position: relative;
    width: 1200px;
    height: 800px;
    overflow: hidden;
    font-family: "Source Sans 3", "Myriad Pro", sans-serif;
    color: var(--ink);
    background: linear-gradient(
      to bottom,
      var(--paper) 6%,
      var(--cream) 17%,
      var(--sun) 31%,
      var(--amber) 41%,
      var(--coral) 49%,
      var(--plum) 54%,
      var(--navy) 59%,
      var(--navy) 62%,
      var(--mist) 69%,
      var(--paper) 76%
    );
  }

  /* faint repeated school name across the colour band */
  .name-pattern {
    position: absolute;
    margin: 0;
    color: var(--ghost);
    font-weight: 400;
    line-height: 1;
    white-space: nowrap;
    pointer-events: none;
  }
  .name-pattern.upper  { left: 285px; top: 160px; font-size: 50px; }
  .name-pattern.wide   { left: 26px;  top: 262px; font-size: 70px; }
  .name-pattern.band   { left: 30px;  top: 350px; font-size: 78px; }
  .name-pattern.right  { left: 610px; top: 252px; font-size: 62px; }
  .name-pattern.small  { left: 262px; top: 500px; font-size: 22px; }
  .name-pattern.low    { left: 450px; top: 452px; font-size: 50px; }
  .name-pattern.edge   { left: 960px; top: 118px; font-size: 44px; }

  /* school name */
  .school-name {
    position: absolute;
    margin: 0;
    font-weight: 400;
    color: var(--ink);
    white-space: nowrap;
    line-height: 1;
  }
  .school-name.top   { left: 24px;  top: 92px;  font-size: 36px; }
  .school-name.front { left: 700px; top: 600px; font-size: 40px; }

  /* quote */
  .quote {
    position: absolute;
    left: 700px;
    top: 182px;
    width: 316px;
    margin: 0;
    text-align: center;
    text-shadow: 1px 1px 2px rgba(255, 255, 255, 0.7);
  }
  .quote p {
    margin: 0;
    font-style: italic;
    font-weight: 600;
    font-size: 27px;
    line-height: 1.4;
  }
  .quote cite {
    display: block;
    margin-top: 8px;
    font-style: normal;
    font-size: 23px;
  }

  /* contact block on back panel */
  .contact {
    position: absolute;
    left: 130px;
    top: 630px;
    width: 366px;
    margin: 0;
    padding: 0;
    list-style: none;
    text-align: center;
    font-size: 31px;
    font-weight: 600;
    line-height: 1.5;
    text-shadow: 1px 1px 2px rgba(0, 0, 0, 0.25);
  }

  /* illustration placeholder */
  .butterfly-art {
    position: absolute;
    left: 986px;
    top: 434px;
    width: 154px;
    height: 146px;
    border-radius: 24px;
    background: linear-gradient(135deg, var(--wing-orange), var(--wing-deep));
  }
</style>
</head>
<body>
  <main class="folder">
    <p class="name-pattern upper" aria-hidden="true">valtrin children's school</p>
    <p class="name-pattern wide" aria-hidden="true">valtrin</p>
    <p class="name-pattern band" aria-hidden="true">children's school</p>
    <p class="name-pattern right" aria-hidden="true">children's school</p>
    <p class="name-pattern edge" aria-hidden="true">valtrin</p>
    <p class="name-pattern small" aria-hidden="true">valtrin children's school</p>
    <p class="name-pattern low" aria-hidden="true">valtrin children's</p>

    <h2 class="school-name top">Valtrin Children's School</h2>

    <blockquote class="quote">
      <p>“Within the child is the person he or she will become”</p>
      <cite>-Dr. Helga Brunvaldi</cite>
    </blockquote>

    <div class="butterfly-art" role="img" aria-label="Illustration of an orange monarch butterfly"></div>

    <h1 class="school-name front">Valtrin Children's School</h1>

    <ul class="contact">
      <li>www.vtschool.org</li>
      <li>Tel. : (415) 555-0147</li>
      <li>Fax : (415) 555-0192</li>
    </ul>
  </main>
</body>
</html>
```